Optimization existing Business Card

I need a revision of the business card, incl. Logo Design. I am a freelancer and have my headquarters in Berlin. I develop business consulting solutions for banks, insurance and StartUp Companies. I want a simple design of the business card. The final design should professionalism and commitment and openness to communicate. I'm open minded in addition to optimizing the existing logo / business card as well on a new idea / proposal for the logo. Idea would be for example the logo of this page: http://morvale-advisory.example.

Target Market(s)

Consulting, Banking, Investment Banking

Industry/Entity Type

Business

Contact Information for Business Card

siehe Anhang (please take a look into the attachments, important)

Font styles to use
Sans Serif

Requirements
Must have
• Please look at my specifications exactly !! (Please see my specifications), CEO Founder not
Should not have
• No gradient !! (No overarching color gradient)

```html
<!DOCTYPE html>
<html lang="de">
<head>
<meta charset="utf-8">
<title>Halvorsen Consulting – Visitenkarte</title>
<link rel="stylesheet" href="https://fonts.googleapis.com/css2?family=Open+Sans:wght@400;600;700&display=swap">
<style>
  :root {
    --stage: #2b2b2d;
    --navy: #3d3b5c;
    --blue: #27a4dd;
    --white: #ffffff;
    --ink: #1c1c24;
  }
  * { box-sizing: border-box; margin: 0; padding: 0; }
  html, body {
    width: 1200px; height: 1166px; overflow: hidden;
    background: var(--stage);
    font-family: "Open Sans", Arial, sans-serif;
  }
  .card {
    position: absolute; left: 158px; width: 884px; height: 520px;
    overflow: hidden; box-shadow: 0 10px 30px rgba(0,0,0,.45);
  }
  .card--back { top: 30px; background: var(--navy); color: var(--white); }
  .card--front { top: 606px; background: var(--white); color: var(--ink); }

  .brand { position: absolute; display: flex; align-items: center; }
  .brand__dot { width: 34px; height: 34px; border-radius: 50%; margin-right: 16px; }
  .brand__name { font-weight: 700; font-size: 38px; line-height: 1; letter-spacing: .5px; }
  .brand__rule { width: 3px; height: 62px; background: var(--blue); margin: 0 16px 0 20px; }
  .brand__services { font-size: 14px; line-height: 1.25; letter-spacing: .6px; text-transform: uppercase; }

  .card--back .brand { left: 150px; top: 220px; }
  .card--back .brand__dot { background: var(--blue); }
  .card--back .brand__name { color: var(--white); }
  .card--back .brand__services { color: var(--white); }
  .card--back .url {
    position: absolute; right: 140px; bottom: 70px;
    font-size: 20px; letter-spacing: 1.4px; color: var(--white);
  }

  .card--front .brand { left: 70px; top: 70px; }
  .card--front .brand__dot { background: var(--blue); }
  .card--front .brand__name { color: var(--navy); }
  .card--front .brand__services { color: var(--navy); }

  .swoosh { position: absolute; inset: 0; }

  .person { position: absolute; right: 80px; top: 190px; text-align: right; }
  .person__name { color: var(--blue); font-weight: 700; font-size: 30px; }
  .person__role { font-size: 20px; color: var(--ink); margin-top: 2px; }

  .contact { position: absolute; left: 90px; top: 300px; list-style: none; }
  .contact li { display: flex; align-items: center; font-size: 23px; line-height: 38px; color: var(--ink); }
  .contact svg { width: 22px; height: 22px; margin-right: 18px; fill: var(--blue); flex: none; }

  .card--front .url {
    position: absolute; right: 60px; bottom: 40px;
    font-size: 21px; letter-spacing: .8px; color: var(--white);
  }
</style>
</head>
<body>

<section class="card card--back" aria-label="Kartenrückseite">
  <div class="brand">
    <span class="brand__dot"></span>
    <span class="brand__name">halvorsen consulting</span>
    <span class="brand__rule"></span>
    <span class="brand__services">Unternehmensberatung<br>Banking<br>Business Coaching</span>
  </div>
  <p class="url">www.halvorsen-consulting.example</p>
</section>

<section class="card card--front" aria-label="Kartenvorderseite">
  <svg class="swoosh" viewBox="0 0 884 520" preserveAspectRatio="none" aria-hidden="true">
    <path d="M290 462 Q 620 420 884 200 L884 236 Q 610 440 290 462 Z" fill="var(--blue)"/>
    <path d="M0 478 Q 560 468 884 256 L884 520 L0 520 Z" fill="var(--navy)"/>
  </svg>

  <div class="brand">
    <span class="brand__dot"></span>
    <span class="brand__name">halvorsen consulting</span>
    <span class="brand__rule"></span>
    <span class="brand__services">Unternehmensberatung<br>Banking<br>Business Coaching</span>
  </div>

  <div class="person">
    <p class="person__name">Jonas Halvorsen</p>
    <p class="person__role">Founder</p>
  </div>

  <ul class="contact">
    <li>
      <svg viewBox="0 0 24 24" aria-hidden="true"><path d="M6.6 10.8a15.1 15.1 0 0 0 6.6 6.6l2.2-2.2c.3-.3.7-.4 1-.2 1.1.4 2.3.6 3.6.6.6 0 1 .4 1 1V20c0 .6-.4 1-1 1A17 17 0 0 1 3 4c0-.6.4-1 1-1h3.5c.6 0 1 .4 1 1 0 1.3.2 2.5.6 3.6.1.3 0 .7-.2 1z"/></svg>
      +49 (0) 30 5550 1827
    </li>
    <li>
      <svg viewBox="0 0 24 24" aria-hidden="true"><path d="M7 2h10a1 1 0 0 1 1 1v18a1 1 0 0 1-1 1H7a1 1 0 0 1-1-1V3a1 1 0 0 1 1-1zm1 3v10h8V5zm4 12.5a1.2 1.2 0 1 0 0 2.4 1.2 1.2 0 0 0 0-2.4z"/></svg>
      +49 (0) 176 5550 3946
    </li>
    <li>
      <svg viewBox="0 0 24 24" aria-hidden="true"><path d="M2 5h20v14H2zm2 2v.4l8 5.2 8-5.2V7zm0 2.8V17h16V9.8l-8 5.2z"/></svg>
      jh@halvorsen-consulting.example
    </li>
  </ul>

  <p class="url">www.halvorsen-consulting.example</p>
</section>

</body>
</html>
```